40-year-old commercial construction firm :: Business Card Revamp

We are a 40 year-old, private general construction company based in Dallas, Texas, and we are considering updating our business cards, which could lead to a larger "brand refresh" campaign.

We work in a competitive environment, selling to business owners and executives making large scale purchasing decisions on behalf of their firms. A majority of our business is repeat business, with a long sales-cycle; while business can be difficult to identify and land, the effort is often rewarded with multiple projects.

We are open to a logo "refresh" as well as designs that incorporate the existing logo.

Target Market(s)

B2B selling to business owners/executives/end users who make facility decisions for their firms.

Industry/Entity Type

Construction Company

Contact Information for Business Card

Refresh from the example provided

Logo Text

Harkel Building Company :: See card example

Font styles to use
Other font styles liked:
• See sample card :: Designers to choose

Colors

Designer to choose colors to be used in the design.

Requirements
Must have
• Design should convey:
• Confidence
• Competence
• Capability
• Stability
• Tagline: Genuine Relationships :: Superior Services :: Environmentally Aware
Nice to have
• A solid design that is transferable from print to online.
• Note that we are also considering a painted-edge printing / card design
Should not have
• Too much color or whimsy. Our clients tend to be the serious type, and we work hard to present a serious, professional presence in the marketplace.

```html
<!DOCTYPE html>
<html lang="en">
<head>
<meta charset="utf-8">
<title>Harkel Building Company – Business Card</title>
<link href="https://fonts.googleapis.com/css2?family=Open+Sans:wght@400;600&display=swap" rel="stylesheet">
<style>
  :root {
    --stage: #e9e7e3;
    --card-dark: #141414;
    --card-dark-2: #262626;
    --card-light: #ffffff;
    --ink: #1b1b1b;
    --ink-soft: #f2f2f2;
    --ink-muted: #9a9a9a;
    --gold: #c8962a;
    --faint: #e6e6e6;
  }
  * { margin: 0; padding: 0; box-sizing: border-box; }
  html, body { width: 1200px; height: 900px; overflow: hidden; }
  body {
    background: var(--stage);
    font-family: "Open Sans", Arial, sans-serif;
    position: relative;
  }
  .card {
    position: absolute;
    width: 560px;
    height: 320px;
    border-radius: 3px;
    box-shadow: 0 10px 28px rgba(0,0,0,.18);
    overflow: hidden;
  }

  /* front */
  .card-front {
    left: 70px; top: 100px;
    background: var(--card-dark);
  }
  .front-texture {
    position: absolute; inset: 0;
    background: radial-gradient(ellipse at 50% 40%, var(--card-dark-2), var(--card-dark) 75%);
  }
  .front-brand {
    position: absolute; left: 0; right: 0; top: 100px;
    text-align: center; color: var(--ink-soft);
  }
  .front-name { font-size: 68px; font-weight: 400; line-height: 1; letter-spacing: -1px; }
  .front-sub { font-size: 19px; letter-spacing: .5px; margin-top: 4px; }
  .tagline {
    position: absolute; left: 0; right: 0; bottom: 34px;
    text-align: center;
    font-size: 11.5px; letter-spacing: 1px;
    color: var(--ink-muted);
    text-transform: uppercase;
  }
  .tagline .sep { color: var(--gold); padding: 0 6px; }

  /* back */
  .card-back {
    left: 570px; top: 470px;
    background: var(--card-light);
    color: var(--ink);
  }
  .back-accent {
    position: absolute; right: -40px; top: -40px;
    width: 260px; height: 260px; border-radius: 50%;
    background: radial-gradient(circle at 45% 55%, var(--faint), rgba(230,230,230,0) 70%);
  }
  .brand-lockup {
    position: absolute; left: 32px; top: 36px;
    display: flex; align-items: center; gap: 12px;
  }
  .brand-square {
    width: 72px; height: 72px;
    border: 3px solid var(--gold);
  }
  .brand-name { font-size: 46px; line-height: .95; letter-spacing: -1px; }
  .brand-sub { font-size: 14px; letter-spacing: .3px; margin-top: 2px; }

  .person { position: absolute; left: 36px; top: 138px; }
  .person-name { color: var(--gold); font-size: 25px; line-height: 1.1; }
  .person-role { font-size: 15px; font-weight: 600; }

  .contact-list { list-style: none; margin-top: 12px; }
  .contact-list li {
    display: flex; align-items: center; gap: 8px;
    font-size: 15px; line-height: 21px;
  }
  .contact-list svg { width: 13px; height: 13px; fill: var(--gold); flex: none; }

  .office {
    position: absolute; right: 26px; top: 196px;
    text-align: right; font-size: 13px; line-height: 17px;
  }
  .office-label { color: var(--gold); }
</style>
</head>
<body>

<section class="card card-front" aria-label="Business card front">
  <div class="front-texture" role="img" aria-label="Subtle tiled brand pattern on black"></div>
  <div class="front-brand">
    <div class="front-name">Harkel</div>
    <div class="front-sub">BUILDING COMPANY, LTD</div>
  </div>
  <p class="tagline">Genuine Relationships<span class="sep">::</span>Superior Services<span class="sep">::</span>Environmentally Aware</p>
</section>

<section class="card card-back" aria-label="Business card back">
  <div class="back-accent" role="img" aria-label="Large faint brand decoration"></div>

  <div class="brand-lockup">
    <div class="brand-square"></div>
    <div>
      <div class="brand-name">Harkel</div>
      <div class="brand-sub">BUILDING COMPANY, LTD</div>
    </div>
  </div>

  <div class="person">
    <div class="person-name">Dean Carver</div>
    <div class="person-role">Business Development</div>
    <ul class="contact-list">
      <li><svg viewBox="0 0 16 16"><path d="M1 5c0-2 2-3 7-3s7 1 7 3v1h-4V5H5v1H1zM3 8h10l2 6H1z"/></svg>972.555.0148</li>
      <li><svg viewBox="0 0 16 16"><path d="M4 0h8v16H4zM5.5 2v10h5V2z"/></svg>214.555.0193</li>
      <li><svg viewBox="0 0 16 16"><path d="M4 0h8v4h3v12H1V4h3zm2 2v4h4V2zM3 8v2h10V8z"/></svg>972.555.0162</li>
      <li><svg viewBox="0 0 16 16"><path d="M0 3h16v10H0zm1.5 1.5 6.5 5 6.5-5z"/></svg>dcarver@harkel.com</li>
      <li><svg viewBox="0 0 16 16"><circle cx="8" cy="8" r="7.5"/></svg>www.harkel.com</li>
    </ul>
  </div>

  <div class="office">
    <div class="office-label">U.S.CORPORATE OFFICE</div>
    <div>1870 Corbin Lane</div>
    <div>Dallas,Texas 75231</div>
  </div>
</section>

</body>
</html>
```